TCH Business cards

We are a medium sized property company based in London and require a logo, Business card which reflects a professional company and incorporates our catchy name.

Our statement is (Building for the future) we like colours such as royal blue, greens and light browns but will look at anything.

Contact Information for Business Card

Tidecrest Holdings Limited
Unit 4, 3-5 Parbrook Lane
London
SE21 7QX

Web: www.tidecrestholdings.example

Email: tidecrestltd@mailbox.example

Telephone: +44-208-555-0142
Fax: +44-208-555-0187

```html
<!DOCTYPE html>
<html lang="en">
<head>
<meta charset="utf-8">
<title>Tidecrest Holdings Limited – Business Card</title>
<link rel="stylesheet" href="https://fonts.googleapis.com/css2?family=Open+Sans:wght@400;600;700&display=swap">
<style>
  :root {
    --page-bg: #e9e7e3;
    --card-bg: #ffffff;
    --brand-blue: #2f5a8f;
    --brand-deep: #1f4677;
    --text-grey: #8a929c;
    --rule-grey: #9aa3ad;
    --decor-tint: #dfe5ec;
    --icon-grey: #7d8894;
  }
  * { margin: 0; padding: 0; box-sizing: border-box; }
  html, body {
    width: 1200px; height: 1023px; overflow: hidden;
    background: var(--page-bg);
    font-family: "Open Sans", Arial, sans-serif;
  }
  .canvas {
    width: 1200px; height: 1023px;
    display: flex; align-items: center; justify-content: center;
  }
  .business-card {
    position: relative;
    width: 960px; height: 548px;
    background: var(--card-bg);
    box-shadow: 0 10px 30px rgba(0,0,0,0.15);
    overflow: hidden;
  }
  .skyline-decor {
    position: absolute; right: 0; top: 0;
    width: 460px; height: 548px;
    background: radial-gradient(ellipse at 80% 20%, var(--decor-tint) 0%, rgba(223,229,236,0.45) 45%, rgba(255,255,255,0) 75%);
  }
  .swoosh { position: absolute; left: 0; top: 0; width: 960px; height: 548px; }
  .company-mark {
    position: absolute; left: 70px; top: 70px;
    display: flex; align-items: flex-start; gap: 22px;
  }
  .company-mark .mark-square {
    width: 70px; height: 70px; background: var(--brand-blue);
    margin-top: 8px;
  }
  .company-name {
    color: var(--brand-blue);
    font-weight: 700; font-size: 44px; line-height: 1.05;
  }
  .holder {
    position: absolute; left: 70px; top: 318px;
    display: flex; align-items: baseline; gap: 12px;
  }
  .holder-name { color: var(--brand-blue); font-weight: 700; font-size: 40px; }
  .holder-divider { width: 2px; height: 38px; background: var(--rule-grey); align-self: center; }
  .holder-role { color: var(--text-grey); font-size: 22px; }
  .address {
    position: absolute; left: 70px; top: 428px;
    color: var(--text-grey); font-size: 22px; line-height: 1.45;
  }
  .contact-list {
    position: absolute; right: 50px; top: 48px;
    list-style: none;
    color: var(--brand-deep); font-size: 21px; line-height: 1.55;
    text-align: right;
  }
  .contact-list li { display: flex; align-items: center; justify-content: flex-end; gap: 12px; }
  .contact-list svg { width: 20px; height: 20px; flex: none; }
</style>
</head>
<body>
<main class="canvas">
  <section class="business-card">
    <div class="skyline-decor" role="img" aria-label="Faint decorative brand graphic"></div>

    <svg class="swoosh" viewBox="0 0 960 548" aria-hidden="true">
      <path d="M30 415 Q520 412 642 322 Q695 285 720 230 Q690 282 636 316 Q516 402 30 415 Z" fill="var(--brand-blue)"/>
    </svg>

    <div class="company-mark">
      <span class="mark-square"></span>
      <div class="company-name">Tidecrest<br>Holdings<br>Limited</div>
    </div>

    <div class="holder">
      <span class="holder-name">Edward Clarke</span>
      <span class="holder-divider"></span>
      <span class="holder-role">Director</span>
    </div>

    <p class="address">Unit 4, 3-5 Parbrook Lane<br>London SE21 7QX</p>

    <ul class="contact-list">
      <li>+44-208-555-0142
        <svg viewBox="0 0 20 20"><rect width="20" height="20" rx="3" fill="var(--icon-grey)"/><path d="M6 4h3l1 4-2 1c1 2 2 3 4 4l1-2 4 1v3c-7 0-12-5-11-11z" fill="#fff"/></svg></li>
      <li>+44-208-555-0187
        <svg viewBox="0 0 20 20"><rect width="20" height="20" rx="3" fill="var(--icon-grey)"/><rect x="6" y="4" width="8" height="4" fill="#fff"/><rect x="4" y="9" width="12" height="5" fill="#fff"/><rect x="6" y="12" width="8" height="4" fill="#fff"/></svg></li>
      <li>tidecrestltd@mailbox.example
        <svg viewBox="0 0 20 20"><rect width="20" height="20" rx="3" fill="var(--icon-grey)"/><rect x="4" y="6" width="12" height="8" fill="#fff"/><path d="M4 6l6 5 6-5" stroke="var(--icon-grey)" stroke-width="1.3" fill="none"/></svg></li>
      <li>www.tidecrestholdings.example
        <svg viewBox="0 0 20 20"><rect width="20" height="20" rx="3" fill="var(--icon-grey)"/><circle cx="10" cy="10" r="5.5" stroke="#fff" stroke-width="1.5" fill="none"/><path d="M4.5 10h11M10 4.5c-3 3-3 8 0 11M10 4.5c3 3 3 8 0 11" stroke="#fff" stroke-width="1.2" fill="none"/></svg></li>
    </ul>
  </section>
</main>
</body>
</html>
```